Flyer-Design für ein Ingenieur- und Planungsbüro
Ein toller Entwurf und freundliche Kommunikation inkl. immer schneller Reaktionszeit, auch wenn es bei mir manchmal mit der Zuarbeit der passenden Bilder gedauert hat. Perfektes Ergebnis!!
Zielgruppe
Ingenieur- und Planungsbüro (Dienstleister) aus Leipzig, welches seit 22 Jahren auf die Optimierung und Neuerrichtung
medizinischer Einrichtungen (Arzt- und Zahnarztpraxen) spezialisiert ist.
Zur Zielgruppe zählen daher Mediziner und Zahnmedizinen zwischen 30 - 55 Jahren, welche bereits eine Praxis führen oder gerade neu gründen möchten. Die Schnittmenge liegt im Praxisstandort = Praxisräume, welche niedergelassene Mediziner zur Ausübung ihrer Tätigkeiten inkl. Personal, Medizintechnik und sonstige Ausstattung benötigen. Der Verkauf von Produkten und Einrichtungen ist nicht meine Aufgabe.
Meine Tätigkeiten liegen in der Beratung, Unterstützung der Medizinerinnen über das gesamte Projekt, von der ersten Idee, über die Umsetzung bis zur Praxiseröffnung. Ich bin daher Lotse, Koordinator aller Projektschnittstellen sowie Planer zur Umsetzung der jeweiligen Kundenanforderungen. Die Leistungsdetails und Stichpunkte sind den Unterlagen zu entnehmen oder weiter zu erfragen.
Aufgabenstellung
Der Flyer soll nach einem telefonischen Erstkontakt oder nach einem persönlichen Treffen meinen potenziellen Kunden einen Überblick zu den Umfangreichen Leistungsportfolio geben. Der Flyer soll professionell und seriös wirken und meine langjährige Expertise und Knowhow vermitteln.
Weiterhin soll der Flyer meinen Netzwerkpartner dienen, welche ebenfalls mit der Zielgruppe der Heilberufe im geschäftlichen Kontakt sind und mich über den Flyer im Gespräch weiterempfehlen und zu einem Neukontakt zwischen dem potenziellen Kunden/ Kundin führen soll.
Der in den Daten zur Verfügung gestellt Entwurf des Flyers braucht nicht 1:1 nachgebaut werden. Er bietet vielmehr eine Orientierung wie ich mir einen Flyer vorstellen kann. Auch die zur Verfügung gestellten Bilden dienen zur Orientierung, ggf. werden diese nach Feststellung des Siegers/ Siegerin im Detail nochmals angepasst.
Farben:
Blau: 041-171-226 / #29abe2
Grün: 140-198-063 / #8cc63f

```html
<!DOCTYPE html>
<html lang="de">
<head>
<meta charset="utf-8">
<title>Praxisbau Werkstatt UG – Flyer</title>
<link href="https://fonts.googleapis.com/css2?family=Montserrat:wght@300;400;500;600;800&display=swap" rel="stylesheet">
<style>
  :root{
    --blue:#4b61a5;
    --green:#a5c33a;
    --grey-panel:#e2e2e2;
    --paper:#f4f4f4;
    --white:#ffffff;
    --text:#3a3a3a;
    --logo-grey:#6e6e6e;
    --bg:#e9e9e9;
  }
  *{margin:0;padding:0;box-sizing:border-box}
  html,body{width:1200px;height:828px;overflow:hidden}
  body{background:var(--bg);font-family:'Montserrat',sans-serif;color:var(--text);position:relative}
  .abs{position:absolute}

  /* Cover */
  .cover{left:100px;top:170px;width:230px;height:490px;background:var(--paper);overflow:hidden;box-shadow:0 8px 20px rgba(0,0,0,.12)}
  .photo{position:absolute}
  .cover-photo{left:0;top:0;width:230px;height:200px;background:linear-gradient(160deg,#f3f1ee,#d9d6d2 60%,#9a8f85)}
  .cover-band{left:0;top:0;width:230px;height:490px}
  .brand{position:absolute;font-family:'Montserrat',sans-serif;font-weight:300;color:var(--logo-grey);line-height:1.15}
  .brand-square{position:absolute;background:var(--green)}
  .cover .brand-square{left:38px;top:220px;width:16px;height:16px}
  .cover .brand{left:32px;top:246px;font-size:15px}
  .headline{left:22px;top:332px}
  .headline span{display:block;font-weight:800;color:var(--blue);font-size:25px;line-height:32px;position:relative}
  .headline span::before{content:"";position:absolute;left:0;top:-3px;width:22px;height:2px;background:var(--green)}
  .headline span:first-child::before{display:none}
  .headline span:last-child::after{content:"";position:absolute;left:0;bottom:-2px;width:22px;height:2px;background:var(--green)}
  .tagline{left:22px;top:448px;font-size:9.5px;letter-spacing:.3px;color:var(--text)}

  /* Inside spread */
  .spread{left:396px;top:170px;width:702px;height:490px;box-shadow:0 8px 20px rgba(0,0,0,.12)}
  .panel{position:absolute;top:0;width:234px;height:490px;overflow:hidden;background:var(--white)}
  .panel-about{left:0}
  .panel-modules{left:234px}
  .panel-service{left:468px}

  .about-top{left:0;top:0;width:234px;height:250px;background:var(--grey-panel)}
  .section-title{position:absolute;font-weight:800;color:var(--blue);font-size:15px;letter-spacing:.5px}
  .about-title{left:22px;top:36px}
  .portrait{left:0;top:56px;width:78px;height:52px;background:linear-gradient(135deg,#6d7482,#2f3442)}
  .about-lead{left:22px;top:58px;width:202px;font-size:7.3px;line-height:11.2px}
  .about-lead .float{float:left;width:60px;height:50px}
  .about-lead b{font-weight:600}
  .about-text{left:22px;width:200px;font-size:7.3px;line-height:11.2px}
  .about-p1{top:134px}
  .about-p2{top:192px}
  .about-photo{left:0;top:250px;width:234px;height:240px;background:linear-gradient(170deg,#b9b6ae,#8d8880 55%,#5d5953)}

  .hall-photo{left:0;top:0;width:234px;height:250px;background:linear-gradient(180deg,#a6a29c,#c9c6c0 45%,#8e8a83)}
  .modules-bottom{left:0;top:250px;width:234px;height:240px;background:var(--green)}
  .panel-modules .brand-square{left:40px;top:198px;width:12px;height:12px}
  .panel-modules .brand{left:18px;top:216px;font-size:12px}
  .modules-title{left:16px;top:296px;color:var(--white);font-size:13.5px}

  .service-title{left:20px;top:68px}
  .service-photo{left:0;top:250px;width:234px;height:240px;background:linear-gradient(170deg,#f2f2f2,#d8dbe0 60%,#a9abae)}

  .list{position:absolute;list-style:none}
  .list li{position:relative;padding-left:11px;margin-bottom:6px}
  .list li::before{content:"";position:absolute;left:0;top:2px;width:6px;height:6px;background:var(--marker)}
  .list li::after{content:"";position:absolute;left:1.5px;top:3.5px;width:2px;height:2px;border-right:1px solid var(--marker-ink);border-top:1px solid var(--marker-ink);transform:rotate(45deg)}
  .modules-list{left:16px;top:320px;width:210px;font-size:7.3px;line-height:10.4px;color:var(--white);--marker:#ffffff;--marker-ink:var(--green)}
  .service-list{left:20px;top:96px;width:204px;font-size:7.5px;line-height:10.8px;--marker:var(--green);--marker-ink:#ffffff}
  .service-list li{margin-bottom:7px}
  .inline-list{--marker:var(--green);--marker-ink:#ffffff}
</style>
</head>
<body>

<section class="abs cover" aria-label="Titelseite">
  <div class="photo cover-photo" role="img" aria-label="Foto eines hellen Behandlungsraums einer Zahnarztpraxis"></div>
  <svg class="abs cover-band" viewBox="0 0 230 490" aria-hidden="true">
    <polygon points="0,200 120,200 140,230 0,230" fill="#f4f4f4"/>
    <polygon points="130,230 230,230 230,266 160,266" fill="var(--blue)"/>
    <rect x="222" y="266" width="8" height="224" fill="#6b7f2a"/>
  </svg>
  <div class="brand-square"></div>
  <div class="brand">Praxisbau<br>Werkstatt UG</div>
  <h1 class="abs headline">
    <span>KONZEPTION</span>
    <span>PLANUNG</span>
    <span>UMSETZUNG</span>
  </h1>
  <p class="abs tagline">EXPERTISE, KNOWHOW, ÜBERSICHT</p>
</section>

<section class="abs spread" aria-label="Innenseiten">

  <article class="panel panel-about">
    <div class="abs about-top"></div>
    <svg class="abs" style="left:0;top:0" width="234" height="40" viewBox="0 0 234 40" aria-hidden="true">
      <polygon points="112,6 150,6 165,28 127,28" fill="var(--green)"/>
      <polygon points="160,6 188,6 203,28 175,28" fill="var(--blue)"/>
    </svg>
    <h2 class="section-title about-title">UBER</h2>
    <div class="abs photo portrait" role="img" aria-label="Porträtfoto des Geschäftsführers"></div>
    <p class="abs about-lead"><span class="float"></span><b>Jens Falkner</b>, Geschäftsführer der Praxisbau Werkstatt UG. Industriemeister, Baufachwirt, Betriebswirt (IHK). Seit 22 Jahren spezialisiert auf ambulante Einrichtungen des Gesundheitswesens.</p>
    <ul class="list about-text about-p1 inline-list">
      <li>Ihr übergreifender Spezialist für alle Schnittstellen und Projektetappen. Professionelle Unterstützung und Lotse für alle Heilberufe rund um Ihren Praxisstandort.</li>
    </ul>
    <ul class="list about-text about-p2 inline-list">
      <li>Für Neugründung, Bestandsoptimierung und Standortsuche. Von der Idee bis zur Praxis-Neueröffnung.</li>
    </ul>
    <div class="photo about-photo" role="img" aria-label="Foto einer Baustelle mit Dämmmaterial vor großen Fenstern"></div>
  </article>

  <article class="panel panel-modules">
    <div class="photo hall-photo" role="img" aria-label="Foto eines leeren Rohbauraums mit Fensterreihe"></div>
    <svg class="abs" style="left:0;top:0" width="234" height="250" viewBox="0 0 234 250" aria-hidden="true">
      <polygon points="0,188 90,188 114,250 0,250" fill="var(--paper)"/>
    </svg>
    <div class="brand-square"></div>
    <div class="brand">Praxisbau<br>Werkstatt UG</div>
    <div class="abs modules-bottom"></div>
    <h2 class="section-title modules-title">LEISTUNGSBAUSTEINE:</h2>
    <ul class="list modules-list">
      <li>Standortsuche, Bewertung, Machbarkeitsprüfung</li>
      <li>Konzeption, Funktionsplanung, Kostenschätzung</li>
      <li>Projektplanung, Terminplanung, Ausbaubeschreibung</li>
      <li>Entwurfs-, Einrichtungs- und Ausführungsplanung</li>
      <li>Ausschreibungen, Leistungsvergabe, Schnittstellenmanagement</li>
      <li>Projekt- und Bauüberwachung, bis zur Praxiseröffnung</li>
    </ul>
  </article>

  <article class="panel panel-service">
    <svg class="abs" style="left:0;top:0" width="234" height="40" viewBox="0 0 234 40" aria-hidden="true">
      <polygon points="0,14 234,0 234,20 0,34" fill="var(--green)"/>
    </svg>
    <h2 class="section-title service-title">SERVICE:</h2>
    <ul class="list service-list">
      <li>unabhängige Leistungen, kein Produktverkauf</li>
      <li>Steuerung und Koordination von Gewerken, Dienstleistern und Technikern</li>
      <li>Management Dritter am Projekt Beteiligter (Vermieter, Bauträger, Dental-/ Medizintechnik, IT, Einrichtung, uvm.)</li>
      <li>volle Kosten und Terminkontrolle</li>
      <li>bedarfsgerechte und flexible Beratung, Unterstützung, Planung</li>
    </ul>
    <div class="photo service-photo" role="img" aria-label="Foto einer hellen Praxisküche mit Arbeitsfläche"></div>
  </article>

</section>
</body>
</html>
```